Propose a revamped landing page

One template we like eg is https://www.trovask.com but but cluttered Our logo and colors are attached to our logo and colors are printed on a white background what we have. So font usage ...
1 page

```html
<!DOCTYPE html>
<html lang="en">
<head>
<meta charset="utf-8">
<title>VoltSaver – Always switch to the cheapest energy provider</title>
<link href="https://fonts.googleapis.com/css2?family=Montserrat:wght@400;500;600;700;800&family=Open+Sans:wght@400;600&display=swap" rel="stylesheet">
<style>
:root{
  --orange:#f15a24;
  --orange-light:#f7931e;
  --amber:#f39c12;
  --dark:#2f3438;
  --teal:#16917f;
  --teal-dark:#2b3a3f;
  --cream:#fdf1e1;
  --ink:#333a3f;
  --muted:#6b7075;
  --white:#ffffff;
  --foot-top:#f3f8fc;
  --foot-bottom:#dbeaf6;
  --foot-bar:#d2e4f3;
}
*{margin:0;padding:0;box-sizing:border-box}
html,body{width:1200px;height:3249px;overflow:hidden}
body{position:relative;background:var(--white);font-family:"Open Sans",Arial,sans-serif;color:var(--ink)}
.abs{position:absolute}
h1,h2,h3,h4,.brand,.btn,.nav a{font-family:"Montserrat",Arial,sans-serif}

/* hero */
.hero-bg{left:0;top:0}
.brand{left:158px;top:28px;color:var(--white);font-weight:800;font-size:36px;line-height:1;letter-spacing:-0.5px;display:flex;align-items:center;gap:10px}
.brand .dot{width:26px;height:26px;border-radius:50%;background:var(--white)}
.nav{left:427px;top:42px;display:flex;gap:24px}
.nav a{color:var(--white);font-weight:600;font-size:15px;text-decoration:none;white-space:nowrap}
.hero-title{left:154px;top:224px;width:470px;color:var(--white);font-size:36px;font-weight:700;line-height:1.02}
.hero-sub{left:160px;top:348px;width:430px;color:#ffe3cf;font-size:15px;line-height:1.45}
.btn{display:flex;align-items:center;justify-content:center;border-radius:30px;font-weight:700;font-size:17px;color:var(--white);text-decoration:none}
.btn-dark{left:149px;top:416px;width:183px;height:55px;background:var(--dark)}
.dots{left:574px;top:535px;display:flex;gap:10px}
.dots span{width:13px;height:13px;border-radius:50%;border:2px solid #fbd3b8}
.dots span.on{background:var(--white);border-color:var(--white)}
.hero-figure{left:705px;top:95px;width:310px;height:615px;border-radius:150px 150px 60px 60px;background:linear-gradient(180deg,#f5b48a 0%,#3f7fc4 40%,#e7eef6 75%,#2e6db8 100%)}

/* intro */
.intro-art{left:184px;top:680px;width:356px;height:420px;border-radius:40px;background:radial-gradient(ellipse at 50% 45%,#e9ecea 0%,#cfd8cf 40%,#a7c86a 70%,rgba(255,255,255,0) 100%)}
.intro-title{left:589px;top:770px;width:440px;font-size:30px;font-weight:700;line-height:1.22;color:var(--ink)}
.intro-text{left:591px;top:865px;width:420px;font-size:15px;line-height:1.55;color:var(--ink)}
.intro-text p+p{margin-top:12px}
.btn-teal{left:591px;top:1020px;width:162px;height:50px;background:var(--teal)}

/* steps */
.band{left:0;top:1150px}
.bolt{width:62px;height:62px;border-radius:50%;background:var(--white);border:4px solid var(--amber);display:flex;align-items:center;justify-content:center}
.steps-title{left:0;width:1200px;top:1268px;text-align:center;color:var(--white);font-size:29px;font-weight:700}
.step{width:270px;text-align:center;color:var(--white)}
.step svg{display:block;margin:0 auto}
.step h3{font-size:21px;font-weight:500;margin-top:16px;line-height:1.2}
.step p{font-size:14px;line-height:1.4;margin-top:8px;color:#dbeeea}
.step-link{left:360px;top:1400px}

/* benefits */
.cream{left:0;top:1680px;width:1200px;height:640px;background:var(--cream)}
.benefits-title{left:0;width:1200px;top:1813px;text-align:center;font-size:29px;font-weight:700;color:var(--ink)}
.card{top:1930px;width:282px;height:230px;background:var(--white);border-radius:8px;box-shadow:0 10px 28px rgba(180,140,90,.18);text-align:center;padding:74px 32px 0}
.card h3{color:var(--teal);font-size:20px;font-weight:700}
.card p{font-size:14px;line-height:1.45;color:var(--muted);margin-top:12px}
.card-icon{width:88px;height:88px;border-radius:50%;background:linear-gradient(135deg,var(--orange-light),var(--orange));display:flex;align-items:center;justify-content:center;top:1887px}

/* pricing */
.pricing-bg{left:0;top:2240px}
.price-figure{left:745px;top:2276px;width:262px;height:548px;border-radius:130px 130px 60px 60px;background:linear-gradient(180deg,#c9875e 0%,#f0a24a 38%,#2f5fae 70%,#f28c28 100%)}
.price-title{left:157px;top:2360px;font-size:31px;font-weight:700;color:var(--orange);white-space:nowrap}
.price-lead{left:158px;top:2418px;font-size:18px;color:var(--ink)}
.price-list{left:158px;top:2462px;width:540px;list-style:none}
.price-list li{display:flex;gap:10px;font-size:17px;line-height:1.4;margin-bottom:10px}
.price-list svg{flex:none;margin-top:3px}
.btn-orange{left:156px;top:2645px;width:160px;height:50px;background:var(--orange)}

/* footer */
.footer-bg{left:0;top:2790px;width:1200px;height:459px;background:linear-gradient(180deg,var(--foot-top),var(--foot-bottom))}
.foot-col{top:2922px}
.foot-col h4{font-size:20px;font-weight:700;color:var(--ink);margin-bottom:16px}
.foot-col ul{list-style:none}
.foot-col li{font-size:15px;color:#4a5156;line-height:25px}
.contact li{display:flex;gap:14px;align-items:flex-start;margin-bottom:14px;line-height:20px}
.social li{display:flex;gap:12px;align-items:center;margin-bottom:8px}
.social .ring{width:24px;height:24px;border-radius:50%;background:#2f5d8a}
.foot-bar{left:0;top:3184px;width:1200px;height:65px;background:var(--foot-bar);display:flex;align-items:center;justify-content:center;font-size:15px;color:#4a5156}
</style>
</head>
<body>

<!-- hero -->
<svg class="abs hero-bg" width="1200" height="660" viewBox="0 0 1200 660" aria-hidden="true">
  <defs>
    <linearGradient id="heroGrad" x1="0" y1="0" x2="1" y2="0.6">
      <stop offset="0" stop-color="#f15a24"/>
      <stop offset="1" stop-color="#f7931e"/>
    </linearGradient>
  </defs>
  <path d="M1110 0 C1080 260 900 560 560 630 C360 668 150 640 0 575 L0 600 C150 660 360 688 560 650 C920 580 1110 280 1140 0 Z" fill="#2f3438"/>
  <path d="M0 0 H1120 C1090 260 900 555 560 625 C360 662 150 635 0 570 Z" fill="url(#heroGrad)"/>
  <path d="M640 120 L1060 0 L900 420 Z" fill="#ffffff" opacity=".08"/>
</svg>
<div class="abs brand">VoltSaver<span class="dot"></span></div>
<nav class="abs nav">
  <a href="#">How it Works</a><a href="#">Price</a><a href="#">Ask</a><a href="#">About Us</a><a href="#">Operation</a><a href="#">Press</a><a href="#">Experience</a>
</nav>
<h1 class="abs hero-title">Always automatically switch to the cheapest energy provider</h1>
<p class="abs hero-sub">Lorem ipsum dolor sit amet consectetuer adipiscing elit Nam cursus Morbi ut mi Nullam enim leo</p>
<a class="abs btn btn-dark" href="#">Register Now</a>
<div class="abs dots"><span></span><span class="on"></span><span></span></div>
<div class="abs hero-figure" role="img" aria-label="Illustrated superhero mascot in blue suit with orange cape, standing with arms crossed"></div>

<!-- intro -->
<div class="abs intro-art" role="img" aria-label="Isometric illustration of a giant light bulb over a green island with power plant, wind turbines and solar panels"></div>
<h2 class="abs intro-title">Never pay too much for electricity &amp; gas again</h2>
<div class="abs intro-text">
  <p>Gone are the days of bad deals, tedious rate comparison and boring exchange forms.</p>
  <p>With the automatic change service for VoltSaver you will never again pay too much for electricity and gas. And that, without touching a finger.</p>
</div>
<a class="abs btn btn-teal" href="#">Learn More</a>

<!-- steps band -->
<svg class="abs band" width="1200" height="560" viewBox="0 1150 1200 560" aria-hidden="true">
  <defs>
    <linearGradient id="bandGrad" x1="0" y1="0" x2="1" y2="0">
      <stop offset="0" stop-color="#2b3a3f"/>
      <stop offset="1" stop-color="#16917f"/>
    </linearGradient>
  </defs>
  <path d="M0 1228 C300 1180 900 1180 1200 1230 V1250 C900 1205 300 1205 0 1250 Z" fill="#f39c12"/>
  <path d="M0 1250 C300 1205 900 1205 1200 1252 V1668 C900 1740 350 1760 0 1712 Z" fill="url(#bandGrad)"/>
  <path d="M520 1752 C800 1745 1020 1710 1200 1668 V1690 C1020 1735 800 1760 520 1752 Z" fill="#f39c12"/>
</svg>
<div class="abs bolt" style="left:569px;top:1154px">
  <svg width="26" height="30" viewBox="0 0 26 30"><path d="M15 1 L3 17 H12 L9 29 L23 12 H14 Z" fill="#2f3438"/></svg>
</div>
<h2 class="abs steps-title">How do I become VoltSaver?</h2>
<svg class="abs step-link" width="480" height="90" viewBox="0 0 480 90" aria-hidden="true">
  <path d="M10 30 C60 -5 120 -5 170 20" fill="none" stroke="#cfe7e2" stroke-width="2" stroke-dasharray="3 5"/>
  <path d="M300 30 C350 70 400 70 460 50" fill="none" stroke="#cfe7e2" stroke-width="2" stroke-dasharray="3 5"/>
</svg>
<div class="abs step" style="left:168px;top:1358px">
  <svg width="170" height="130" viewBox="0 0 170 130" aria-hidden="true">
    <path d="M44 20 L62 8 V112" fill="none" stroke="#fff" stroke-width="4"/>
    <circle cx="104" cy="66" r="58" fill="none" stroke="#fff" stroke-width="2" opacity=".8"/>
    <rect x="84" y="46" width="36" height="40" fill="none" stroke="#fff" stroke-width="3"/>
    <path d="M74 66 H108 M98 56 L108 66 L98 76" fill="none" stroke="#fff" stroke-width="3"/>
  </svg>
  <h3>Once login</h3>
  <p>upload financial statements. Select preferences. Finish the registration.</p>
</div>
<div class="abs step" style="left:478px;top:1358px">
  <svg width="170" height="130" viewBox="0 0 170 130" aria-hidden="true">
    <path d="M38 30 C40 0 88 0 86 34 C84 60 40 80 38 112 H90" fill="none" stroke="#fff" stroke-width="4"/>
    <circle cx="110" cy="66" r="58" fill="none" stroke="#fff" stroke-width="2" opacity=".8"/>
    <circle cx="104" cy="64" r="14" fill="none" stroke="#fff" stroke-width="3"/>
    <circle cx="130" cy="52" r="10" fill="none" stroke="#fff" stroke-width="3"/>
    <circle cx="130" cy="80" r="8" fill="none" stroke="#fff" stroke-width="3"/>
  </svg>
  <h3>Automatic</h3>
  <p>fare change We pick the cheapest fare for you and carry out the change automatically.</p>
</div>
<div class="abs step" style="left:783px;top:1358px">
  <svg width="170" height="130" viewBox="0 0 170 130" aria-hidden="true">
    <path d="M40 22 C60 4 92 12 86 40 C82 56 64 60 58 60 C72 60 92 66 88 92 C84 116 50 118 38 100" fill="none" stroke="#fff" stroke-width="4"/>
    <circle cx="112" cy="66" r="58" fill="none" stroke="#fff" stroke-width="2" opacity=".8"/>
    <ellipse cx="114" cy="70" rx="22" ry="17" fill="none" stroke="#fff" stroke-width="3"/>
    <circle cx="116" cy="44" r="7" fill="none" stroke="#fff" stroke-width="3"/>
  </svg>
  <h3>Sit back and<br>Save money</h3>
  <p>Always switch automatically to the low fare.</p>
</div>

<!-- benefits -->
<div class="abs cream"></div>
<h2 class="abs benefits-title">Register once, always save</h2>
<div class="abs card" style="left:173px">
  <h3>Independently</h3>
  <p>We work only for you. In order to remain independent, we consciously do without commission deals with energy providers</p>
</div>
<div class="abs card" style="left:490px">
  <h3>Automatically</h3>
  <p>You sign up once and we'll do the rest. All automatically.</p>
</div>
<div class="abs card" style="left:808px">
  <h3>Fair</h3>
  <p>VoltSaver stays more in Börsel. Despite service charge.</p>
</div>
<div class="abs card-icon" style="left:270px">
  <svg width="44" height="44" viewBox="0 0 44 44" aria-hidden="true"><path d="M40 4 L4 20 L18 24 L22 40 Z M18 24 L40 4" fill="none" stroke="#fff" stroke-width="3" stroke-linejoin="round"/></svg>
</div>
<div class="abs card-icon" style="left:587px">
  <svg width="44" height="44" viewBox="0 0 44 44" aria-hidden="true"><circle cx="22" cy="22" r="7" fill="none" stroke="#fff" stroke-width="3"/><circle cx="22" cy="22" r="15" fill="none" stroke="#fff" stroke-width="3" stroke-dasharray="6 4"/></svg>
</div>
<div class="abs card-icon" style="left:905px">
  <svg width="44" height="44" viewBox="0 0 44 44" aria-hidden="true"><circle cx="22" cy="22" r="18" fill="none" stroke="#fff" stroke-width="3"/><path d="M28 15 C26 12 16 12 16 18 C16 24 28 20 28 27 C28 32 18 32 15 28 M22 9 V35" fill="none" stroke="#fff" stroke-width="3"/></svg>
</div>

<!-- pricing -->
<svg class="abs pricing-bg" width="1200" height="90" viewBox="0 2240 1200 90" aria-hidden="true">
  <path d="M0 2296 C300 2220 800 2230 1200 2300 V2330 H0 Z" fill="#ffffff"/>
</svg>

<!-- footer background -->
<div class="abs footer-bg"></div>
<svg class="abs" style="left:0;top:2760px" width="1200" height="90" viewBox="0 2760 1200 90" aria-hidden="true">
  <path d="M0 2772 C300 2845 900 2845 1200 2772 V2790 C900 2838 300 2838 0 2790 Z" fill="#ffffff"/>
  <path d="M0 2780 C300 2838 900 2838 1200 2780" fill="none" stroke="#f39c12" stroke-width="4"/>
</svg>

<div class="abs price-figure" role="img" aria-label="Illustrated superhero mascot in orange and blue suit with cape, arms crossed"></div>
<h2 class="abs price-title">The Cheapest of all Super Powers</h2>
<p class="abs price-lead">From 24 euros you are there:+</p>
<ul class="abs price-list">
  <li><svg width="18" height="18" viewBox="0 0 18 18" aria-hidden="true"><circle cx="9" cy="9" r="8" fill="none" stroke="#16917f" stroke-width="2"/><path d="M5 9 L8 12 L13 6" fill="none" stroke="#16917f" stroke-width="2"/></svg>Service for electricity or gas (1 meter): 24 euros / year</li>
  <li><svg width="18" height="18" viewBox="0 0 18 18" aria-hidden="true"><circle cx="9" cy="9" r="8" fill="none" stroke="#16917f" stroke-width="2"/><path d="M5 9 L8 12 L13 6" fill="none" stroke="#16917f" stroke-width="2"/></svg>Service for electricity and gas (2 counters): 36 Euro / year</li>
  <li><svg width="18" height="18" viewBox="0 0 18 18" aria-hidden="true"><circle cx="9" cy="9" r="8" fill="none" stroke="#16917f" stroke-width="2"/><path d="M5 9 L8 12 L13 6" fill="none" stroke="#16917f" stroke-width="2"/></svg>The first fee will be charged only after your first change</li>
  <li><svg width="18" height="18" viewBox="0 0 18 18" aria-hidden="true"><circle cx="9" cy="9" r="8" fill="none" stroke="#16917f" stroke-width="2"/><path d="M5 9 L8 12 L13 6" fill="none" stroke="#16917f" stroke-width="2"/></svg>Save up to 850 euros annually electricity and gas costs at the first change *</li>
</ul>
<a class="abs btn btn-orange" href="#">Learn More</a>

<div class="abs bolt" style="left:571px;top:2798px">
  <svg width="26" height="30" viewBox="0 0 26 30"><path d="M15 1 L3 17 H12 L9 29 L23 12 H14 Z" fill="#2f3438"/></svg>
</div>

<div class="abs foot-col contact" style="left:173px">
  <h4>Contact Us</h4>
  <ul>
    <li><svg width="16" height="20" viewBox="0 0 16 20" aria-hidden="true"><path d="M8 19 C3 12 1 9 1 7 A7 7 0 0 1 15 7 C15 9 13 12 8 19 Z" fill="none" stroke="#333a3f" stroke-width="1.6"/><circle cx="8" cy="7" r="2.5" fill="none" stroke="#333a3f" stroke-width="1.6"/></svg><span>42 Harbor Lane #5<br>Austin 78701 TX</span></li>
    <li><svg width="16" height="16" viewBox="0 0 16 16" aria-hidden="true"><path d="M3 1 L6 1 L7 5 L5 6 C6 9 7 10 10 11 L11 9 L15 10 L15 13 C15 14 14 15 13 15 C6 15 1 10 1 3 C1 2 2 1 3 1 Z" fill="none" stroke="#333a3f" stroke-width="1.5"/></svg><span>555.014.2280</span></li>
    <li><svg width="18" height="14" viewBox="0 0 18 14" aria-hidden="true"><rect x="1" y="1" width="16" height="12" fill="none" stroke="#333a3f" stroke-width="1.5"/><path d="M1 1 L9 8 L17 1" fill="none" stroke="#333a3f" stroke-width="1.5"/></svg><span>hello@voltsaver.example</span></li>
  </ul>
</div>
<div class="abs foot-col" style="left:431px">
  <h4>Quick Links</h4>
  <ul><li>How it Works</li><li>Price</li><li>Ask</li><li>About Us</li><li>Operation</li></ul>
</div>
<div class="abs foot-col" style="left:645px">
  <h4>Resources</h4>
  <ul><li>Press</li><li>Experience</li><li>Support</li><li>FAQ</li><li>Contact Us</li></ul>
</div>
<div class="abs foot-col social" style="left:842px">
  <h4>Get in touch</h4>
  <ul>
    <li><span class="ring"></span>Chirper</li>
    <li><span class="ring"></span>FaceLink</li>
    <li><span class="ring"></span>WorkNet</li>
    <li><span class="ring"></span>Snapgram</li>
  </ul>
</div>
<div class="abs foot-bar">Copyright © 2019 All right reserved</div>

</body>
</html>
```